Ceate a flashy Car Cruise-In Flyer for Christian Car Club

Design a flyer for a Christian car club cruise-in at a local restaurant, Bartlos. Should include a car, truck and motorcycle. I'd like it to be striking and suitable for print and post on social media.

Pictures of a car, truck and motorcycle

Info to Include:
Every 3rd Sunday from April-October
Time: 1:30 pm
Location: Bartlo's
4713 SE Fenwick Ave.
Murfreesboro

Website: Halvorine42.example

No preference in colors but should include and contrast with the included Halvorine logo. Also, examples of flyers are included of items I like. I would also like the vehicles to be later model so as not to scare people away that dont own classics. Maybe include an area that says: Exotic cars, Sports Cars, Muscle Cars, Tarvics, Trucks and Motorcycles.

I am not sure what else to add to continue the project.

Target Market(s)

Christian car, truck and motorcycle enthusiasts

Industry/Entity Type

Automotive

Font styles to use
Serif

Requirements
Must have
• Pictures of a car, truck and motorcycle
• Info to Include:
• Every 3rd Sunday from April-October
• Time: 1:30 pm
• Location: Bartlo's
• 4713 SE Fenwick Ave.
• Murfreesboro
• Website: Halvorine42.example
Nice to have
• All cars, trucks, and motorcycles welcome

```html
<!DOCTYPE html>
<html lang="en">
<head>
<meta charset="utf-8">
<title>Halvorine Cruise In Flyer</title>
<link rel="stylesheet" href="https://fonts.googleapis.com/css2?family=Archivo:wdth,wght@125,400;125,700;125,900&display=swap">
<style>
  :root {
    --page-bg: #d9d6d2;
    --paper: #ececec;
    --paper-shade: #dcdcdc;
    --ink: #0d0d0d;
    --red: #e50914;
    --red-deep: #b9060f;
    --white: #ffffff;
    --platform: #1a1a1a;
    --platform-top: #5a5a5a;
  }
  * { margin: 0; padding: 0; box-sizing: border-box; }
  html, body { width: 1200px; height: 1200px; overflow: hidden; }
  body {
    background: var(--page-bg);
    font-family: "Archivo", "Arial Black", sans-serif;
    font-stretch: 125%;
    position: relative;
  }
  .flyer {
    position: absolute;
    left: 160px; top: 30px;
    width: 880px; height: 1140px;
    background: radial-gradient(ellipse at 50% 60%, var(--paper) 0%, var(--paper-shade) 100%);
    overflow: hidden;
    box-shadow: 0 6px 24px rgba(0,0,0,.25);
  }
  .backdrop {
    position: absolute; left: 0; top: 0; width: 100%; height: 560px;
    background: linear-gradient(180deg, #e2e2e2 0%, #c4c4c4 55%, #b0b0b0 100%);
  }
  .brand {
    position: absolute; top: 62px; left: 0; width: 100%;
    text-align: center;
    font-weight: 900; font-size: 66px; letter-spacing: 2px;
    color: var(--red); text-transform: uppercase;
  }
  .brand-mark {
    display: inline-block; width: 22px; height: 22px;
    background: var(--ink); border-radius: 50%;
    margin-right: 16px; vertical-align: middle; position: relative; top: -6px;
  }
  .vehicles {
    position: absolute; left: 0; top: 170px; width: 100%; height: 420px;
  }
  .vehicles svg { width: 100%; height: 100%; display: block; }
  .headline {
    position: absolute; top: 610px; left: 0; width: 100%;
    text-align: center; font-weight: 900; font-size: 128px; line-height: 1;
    color: var(--ink); -webkit-text-stroke: 2px var(--red);
    letter-spacing: 1px;
  }
  .schedule {
    position: absolute; top: 760px; left: 0; width: 100%;
    text-align: center; font-weight: 900; line-height: 1.1; text-transform: uppercase;
  }
  .schedule .day { color: var(--red); font-size: 54px; }
  .schedule .season { color: var(--ink); font-size: 50px; }
  .time-band {
    position: absolute; top: 900px; left: 0; width: 100%; height: 84px;
    background: linear-gradient(90deg, rgba(229,9,20,0) 0%, var(--red) 22%, var(--red-deep) 50%, var(--red) 78%, rgba(229,9,20,0) 100%);
    display: flex; align-items: center; justify-content: center;
    color: var(--white); font-weight: 900; font-size: 62px; text-transform: uppercase;
  }
  .location {
    position: absolute; top: 1002px; left: 0; width: 100%; text-align: center;
  }
  .location .label { font-weight: 700; font-size: 20px; letter-spacing: 2px; color: var(--ink); }
  .location .address { font-weight: 700; font-size: 32px; color: var(--red); margin-top: 2px; }
  .web-bar {
    position: absolute; top: 1080px; left: 170px; width: 540px; height: 44px;
    background: var(--ink);
    clip-path: polygon(0 0, 100% 0, 97% 100%, 3% 100%);
    display: flex; align-items: center; justify-content: center;
    color: var(--white); font-weight: 400; font-size: 18px; letter-spacing: 3px;
  }
</style>
</head>
<body>
  <main class="flyer">
    <div class="backdrop" role="img" aria-label="Silver mosaic tile pattern fading into light grey"></div>

    <div class="brand"><span class="brand-mark"></span>Halvorine</div>

    <div class="vehicles">
      <svg viewBox="0 0 880 420" preserveAspectRatio="none">
        <ellipse cx="450" cy="350" rx="400" ry="62" fill="var(--platform)"/>
        <ellipse cx="450" cy="338" rx="392" ry="56" fill="var(--platform-top)"/>
        <rect x="110" y="40" width="680" height="300" rx="40" fill="url(#vehicleTone)"
              role="img" aria-label="Black motorcycle, red sedan and white camper van side by side on a dark round stage"/>
        <defs>
          <linearGradient id="vehicleTone" x1="0" y1="0" x2="1" y2="0">
            <stop offset="0" stop-color="#2a2a2a"/>
            <stop offset="0.45" stop-color="#c8141c"/>
            <stop offset="1" stop-color="#f1f1f1"/>
          </linearGradient>
        </defs>
      </svg>
    </div>

    <h1 class="headline">CRUISE IN</h1>

    <div class="schedule">
      <div class="day">Every 3rd Sunday</div>
      <div class="season">From April–October</div>
    </div>

    <div class="time-band">Time: 1:30 PM</div>

    <div class="location">
      <div class="label">LOCATION:</div>
      <div class="address">Bartlo's - 4713 SE Fenwick Ave.</div>
    </div>

    <div class="web-bar">www.Halvorine42.example</div>
  </main>
</body>
</html>
```